non prof needs power point design template

The Calloway Trust is a non profit financing and services organization. We are looking for creative ppt templates for various presentations. Including general org overview. marketing and ad decks, etc... Please utilize logo for inspiration for template. We like to communicate to our partners that we are a "business evolved" to served social causes and the public good.
We are launching next year. As such we do not have any other materials. I''m hoping you can provide a creative feel. Yes we''d like a cover page. Several slide templates for different content. Bullet points, graphs, charts, maps, statistics, combos, org charts, flow charts etc...
we work in the following sectors Agriculture and Food Accessibility, Energy, Education, Healthcare, Water/Waste Management, Housing, Emergency Services, Transportation Infrastructure, and Innovative Technologies.
Each relating to economic, food, health, environmental, personal, community, and political security.
Hope that helps.
Non Profit

```html
<!DOCTYPE html>
<html lang="en">
<head>
<meta charset="utf-8">
<title>The Calloway Trust – Presentation Template</title>
<link href="https://fonts.googleapis.com/css2?family=Open+Sans:wght@300;400;600;700&display=swap" rel="stylesheet">
<style>
  :root{
    --stage:#c8c9cb;
    --green:#8ab548;
    --green-soft:#9cc25d;
    --green-deep:#6f9a35;
    --blue:#2f80c6;
    --slate:#5f6062;
    --ink:#555;
    --muted:#8a8a8a;
    --rule:#9a9a9a;
    --white:#fff;
  }
  *{box-sizing:border-box;margin:0;padding:0}
  html,body{width:1200px;height:900px;overflow:hidden}
  body{background:var(--stage);font-family:"Open Sans",Arial,sans-serif;position:relative}
  .slide{position:absolute;width:357px;height:275px;background:var(--white);overflow:hidden}
  .slide-title{position:absolute;left:22px;top:14px;width:313px;font-weight:300;font-size:13px;color:var(--green);
    border-bottom:1px solid var(--rule);padding-bottom:1px;letter-spacing:.2px;line-height:16px}
  .footer-band{position:absolute;left:0;bottom:0;width:100%;height:7px;background:var(--green)}
  .page-num{position:absolute;right:4px;bottom:0;font-size:4px;color:var(--white);line-height:7px}
  .brand-mark{position:absolute;left:10px;bottom:14px;display:flex;align-items:center;gap:3px;
    font-size:6px;font-weight:600;color:var(--slate);letter-spacing:.3px}
  .brand-mark i{display:block;width:6px;height:6px;background:var(--green)}
  .fine{font-size:4.6px;line-height:6.8px;color:var(--muted);text-align:center}

  /* services */
  .service{position:absolute;top:85px;width:100px;text-align:center}
  .service-icon{width:42px;height:42px;border-radius:50%;margin:0 auto 14px;display:flex;align-items:center;justify-content:center}
  .service h3{font-size:8.5px;font-weight:600;margin-bottom:4px}
  .s-green .service-icon{background:var(--green)} .s-green h3{color:var(--green)}
  .s-slate .service-icon{background:var(--slate)} .s-slate h3{color:var(--slate)}
  .s-blue .service-icon{background:var(--blue)} .s-blue h3{color:var(--blue)}

  /* team */
  .team-intro{position:absolute;left:40px;top:70px;width:280px}
  .member{position:absolute;top:90px;width:84px;text-align:center}
  .portrait{width:52px;height:52px;border-radius:50%;margin:0 auto 10px;border:1.5px solid var(--blue);padding:2px}
  .portrait span{display:block;width:100%;height:100%;border-radius:50%;background:linear-gradient(160deg,#d9d9d9,#8c8c8c)}
  .member h4{font-size:6.5px;font-weight:400;color:var(--blue);line-height:8px}
  .member .role{font-size:4.8px;color:var(--muted);margin-bottom:10px}
  .member .bio{font-size:5.3px;line-height:9.8px;color:var(--ink);text-align:justify}

  /* partners */
  .partner-board{position:absolute;left:44px;top:52px;width:270px;height:146px;border:1px solid #ddd;
    display:grid;grid-template-columns:repeat(4,1fr);grid-template-rows:repeat(4,1fr);padding:12px 14px;gap:8px 14px}
  .badge{align-self:center;justify-self:center;width:44px;height:14px;border-radius:2px}
  .b1{background:#e2231a}.b2{background:#2a2a2a}.b3{background:#1d3f8f}.b4{background:#0f1b3d;width:22px;height:22px}
  .b5{background:#2e84c9}.b6{background:#333}.b7{background:#3a7a3a}.b8{background:#d21f1f;width:22px}
  .b9{background:#2b3a8c;width:30px}.b10{background:#e35a2b;width:34px}.b11{background:#3a8a45}.b12{background:#e8c640;width:22px;height:22px;border-radius:50%}
  .b13{background:#1d3f8f}.b14{background:#7d8ea5}.b15{background:#1a3d8c}.b16{background:#2f80c6;width:36px}
  .partner-note{position:absolute;left:44px;top:208px;width:280px;font-size:5.8px;line-height:12.6px;color:var(--muted)}

  /* image & text */
  .panel-green{position:absolute;left:0;top:0;width:176px;height:100%;background:var(--green);color:var(--white)}
  .panel-green .heading{position:absolute;left:14px;top:16px;font-size:12px;font-weight:300}
  .panel-green h3{position:absolute;left:19px;top:96px;font-size:7.6px;font-weight:400}
  .panel-green p{position:absolute;left:19px;top:110px;width:143px;font-size:5.9px;line-height:12.6px;color:#eef5e2;text-align:justify;font-weight:300}
  .panel-green .brand-mark{color:var(--white);left:11px;bottom:12px}
  .panel-green .brand-mark i{background:var(--white)}
  .photo-fill{position:absolute;right:0;top:0;width:181px;height:100%;background:linear-gradient(160deg,#a86a4a,#5b2f28 60%,#3a2a2a)}

  /* section */
  .section-fill{position:absolute;inset:0;background:linear-gradient(180deg,#82ae44,#93bd55 45%,#9cc460)}
  .info-icon{position:absolute;left:149px;top:131px;width:46px;height:46px;border-radius:50%;background:var(--white);
    display:flex;align-items:center;justify-content:center;font:italic 700 30px "Open Sans",serif;color:var(--green)}
  .section-rule{position:absolute;left:122px;top:185px;width:101px;height:1px;background:#e3efd1}
  .section-label{position:absolute;left:0;width:100%;top:190px;text-align:center;font-size:12px;font-weight:300;color:var(--white)}

  /* thank you */
  .closing-top{position:absolute;left:0;top:0;width:100%;height:99px;background:var(--white);display:flex;align-items:center;padding-left:24px;gap:8px}
  .closing-top i{display:block;width:18px;height:18px;background:var(--green)}
  .closing-top span{font-size:17px;font-weight:300;letter-spacing:2px;color:var(--slate)}
  .closing-body{position:absolute;left:0;top:99px;width:100%;bottom:0;background:linear-gradient(120deg,#8ab548,#93bc55)}
  .closing-body::before{content:"";position:absolute;left:0;top:0;width:100%;height:4px;background:#d8d8d8;opacity:.6}
  .thanks{position:absolute;left:21px;top:34px;font-size:12px;font-weight:300;color:var(--white)}
  .contact{position:absolute;left:21px;display:flex;align-items:center;gap:6px;font-size:5.2px;line-height:7px;color:#f1f7e6}
  .contact svg{flex:none}
</style>
</head>
<body>

<!-- Our Services -->
<section class="slide" style="left:50px;top:136px">
  <h2 class="slide-title">OUR SERVICES</h2>
  <div class="service s-green" style="left:20px">
    <div class="service-icon"><svg width="22" height="22" viewBox="0 0 22 22"><circle cx="11" cy="11" r="7" fill="none" stroke="#fff" stroke-width="3.5" stroke-dasharray="3 2.5"/><circle cx="11" cy="11" r="5" fill="#fff"/><circle cx="11" cy="11" r="2.3" fill="#8ab548"/></svg></div>
    <h3>OUR SERVICES</h3>
    <p class="fine">dolor sit amet, consectetur adipiscing elit, sed do eiusmod tempor incididunt ut labore et dolore magna aliqua. Ut enim ad minim veniam, quis nostrud exercitation ullamco laboris nisi ut aliquip ex ea esse cillum dolore eu fugiat nulla pariatur.</p>
  </div>
  <div class="service s-slate" style="left:128px">
    <div class="service-icon"><svg width="22" height="22" viewBox="0 0 22 22"><rect x="4" y="12" width="4" height="7" fill="#fff"/><rect x="9.5" y="9" width="4" height="10" fill="#fff"/><rect x="15" y="11" width="4" height="8" fill="#fff"/><path d="M4 9 L10 5 L13 7 L18 3" stroke="#fff" stroke-width="1.6" fill="none"/></svg></div>
    <h3>OUR SERVICES</h3>
    <p class="fine">dolor sit amet, consectetur adipiscing elit, sed do eiusmod tempor incididunt ut labore et dolore magna aliqua. Ut enim ad minim veniam, quis nostrud exercitation ullamco laboris nisi ut aliquip ex ea esse cillum dolore eu fugiat nulla pariatur.</p>
  </div>
  <div class="service s-blue" style="left:240px">
    <div class="service-icon"><svg width="22" height="22" viewBox="0 0 22 22"><rect x="3" y="4" width="16" height="1.8" fill="#fff"/><rect x="4.5" y="6" width="13" height="9" fill="none" stroke="#fff" stroke-width="1.6"/><path d="M11 15 V18 M8 19 L11 16 L14 19" stroke="#fff" stroke-width="1.5" fill="none"/></svg></div>
    <h3>OUR SERVICES</h3>
    <p class="fine">dolor sit amet, consectetur adipiscing elit, sed do eiusmod tempor incididunt ut labore et dolore magna aliqua. Ut enim ad minim veniam, quis nostrud exercitation ullamco laboris nisi ut aliquip ex ea esse cillum dolore eu fugiat nulla pariatur.</p>
  </div>
  <div class="brand-mark"><i></i>The Calloway Trust</div>
  <div class="footer-band"></div><span class="page-num">2</span>
</section>

<!-- Our Team -->
<section class="slide" style="left:422px;top:136px">
  <h2 class="slide-title">OUR TEAM</h2>
  <p class="team-intro fine">dolor sit amet, consectetur adipiscing elit, sed do eiusmod tempor incididunt ut labore et dolore magna aliqua. Ut enim ad minim veniam, quis nostrud exercitation ullamco laboris nisi ut a</p>
  <div class="member" style="left:32px">
    <div class="portrait" role="img" aria-label="Portrait photo of team member"><span></span></div>
    <h4>JONATHAN DOE</h4><p class="role">President</p>
    <p class="bio">dolor sit amet, consectetur adipiscing elit, sed do eiusmod tempor incididunt ut labore et dolore magna aliqua. Ut enim ad minim veniam, quis nostrud</p>
  </div>
  <div class="member" style="left:133px">
    <div class="portrait" role="img" aria-label="Portrait photo of team member"><span></span></div>
    <h4>MELANIE DOE</h4><p class="role">CEO / Founder</p>
    <p class="bio">dolor sit amet, consectetur adipiscing elit, sed do eiusmod tempor incididunt ut labore et dolore magna aliqua. Ut enim ad minim veniam, quis nostrud</p>
  </div>
  <div class="member" style="left:233px">
    <div class="portrait" role="img" aria-label="Portrait photo of team member"><span></span></div>
    <h4>NATALIE DOE</h4><p class="role">Vice President</p>
    <p class="bio">dolor sit amet, consectetur adipiscing elit, sed do eiusmod tempor incididunt ut labore et dolore magna aliqua. Ut enim ad minim veniam, quis nostrud</p>
  </div>
  <div class="brand-mark"><i></i>The Calloway Trust</div>
  <div class="footer-band"></div><span class="page-num">2</span>
</section>

<!-- Our Partners -->
<section class="slide" style="left:794px;top:136px">
  <h2 class="slide-title">OUR PARTNERS</h2>
  <div class="partner-board" role="img" aria-label="Grid of partner badges">
    <span class="badge b1"></span><span class="badge b2"></span><span class="badge b3"></span><span class="badge b4"></span>
    <span class="badge b5"></span><span class="badge b6"></span><span class="badge b7"></span><span class="badge b8"></span>
    <span class="badge b9"></span><span class="badge b10"></span><span class="badge b11"></span><span class="badge b12"></span>
    <span class="badge b13"></span><span class="badge b14"></span><span class="badge b15"></span><span class="badge b16"></span>
  </div>
  <p class="partner-note">Lorem ipsum dolor sit amet, consectetur adipisicing elit, sed do eiusmod tempor incididunt ut labore et dolore magna aliqua. Ut enim ad minim veniam, quis nostrud exercitation ullamco</p>
  <div class="brand-mark"><i></i>The Calloway Trust</div>
  <div class="footer-band"></div><span class="page-num">2</span>
</section>

<!-- Image & Text -->
<section class="slide" style="left:50px;top:428px;height:276px">
  <div class="panel-green">
    <h2 class="heading">IMAGE &amp; TEXT</h2>
    <h3>LOREM IPSUM DOLOR SIT MET</h3>
    <p>Lorem ipsum dolor sit amet, consectetur adipisicing elit, sed do eiusmod tempor incididunt ut labore et dolore magna aliqua. Ut enim ad minim veniam, quis nostrud exercitation ullamco laboris nisi ut aliquip ex ea commodo consequat. Duis aute irure dolor in reprehenderit in voluptate velit esse cillum dolore eu fugiat nulla pariatur.</p>
    <div class="brand-mark"><i></i>The Calloway Trust</div>
  </div>
  <div class="photo-fill" role="img" aria-label="Photo of smiling schoolchildren gathered close together"></div>
</section>

<!-- Section Title -->
<section class="slide" style="left:420px;top:428px;height:277px">
  <div class="section-fill" role="img" aria-label="Green-tinted photo of a class of children standing in front of a chalkboard"></div>
  <div class="info-icon">i</div>
  <div class="section-rule"></div>
  <h2 class="section-label">SECTION TITLE</h2>
</section>

<!-- Thank You -->
<section class="slide" style="left:794px;top:430px;height:276px">
  <div class="closing-top"><i></i><span>The Calloway Trust</span></div>
  <div class="closing-body">
    <h2 class="thanks">THANK YOU</h2>
    <div class="contact" style="top:80px">
      <svg width="9" height="9" viewBox="0 0 10 10"><circle cx="5" cy="5" r="5" fill="#fff"/><path d="M5 2.2a1.8 1.8 0 0 0-1.8 1.8C3.2 5.5 5 7.8 5 7.8S6.8 5.5 6.8 4A1.8 1.8 0 0 0 5 2.2z" fill="#8ab548"/></svg>
      <span>410 Harbor Lane Suite 12<br>Millbrook, Oregon 97001</span>
    </div>
    <div class="contact" style="top:100px">
      <svg width="9" height="9" viewBox="0 0 10 10"><circle cx="5" cy="5" r="5" fill="#fff"/><path d="M3.2 2.6l1 1.2-.6.7a4 4 0 0 0 1.9 1.9l.7-.6 1.2 1-.6 1C4.6 7.6 2.4 5.4 2.2 3.2z" fill="#8ab548"/></svg>
      <span>1.800.555.0142</span>
    </div>
    <div class="contact" style="top:118px">
      <svg width="9" height="9" viewBox="0 0 10 10"><circle cx="5" cy="5" r="5" fill="#fff"/><rect x="2.6" y="3.3" width="4.8" height="3.4" fill="none" stroke="#8ab548" stroke-width=".8"/><path d="M2.6 3.3L5 5.2l2.4-1.9" fill="none" stroke="#8ab548" stroke-width=".8"/></svg>
      <span>hello@callowaytrust.org</span>
    </div>
    <div class="contact" style="top:136px">
      <svg width="9" height="9" viewBox="0 0 10 10"><circle cx="5" cy="5" r="5" fill="#fff"/><circle cx="5" cy="5" r="2.6" fill="none" stroke="#8ab548" stroke-width=".8"/><path d="M2.4 5h5.2M5 2.4v5.2" stroke="#8ab548" stroke-width=".6"/></svg>
      <span>www.callowaytrust.org</span>
    </div>
  </div>
</section>

</body>
</html>
```